Professional Lawn Treatment flyer (double sided) needed for established gardening company

We are an established and trusted gardening company in Swindon, UK, and are about to launch a new Lawn Treatment Service. This will be marketed to both existing and new customers and needs to reflect our current professional image. The flyer will need to be double-sided, portrait orientation and correctly sized so to be printed on A5.

If you look on our website www.tavistrowgardening.co.uk, you will see our colours are purple and green. We would like you to use these exact shades of purple and green in your design.

As part of the design, we will need you to put together an infographic table to show our packages. I have attached a spreadsheet which explains these packages but I will need you to create a visually appealing table that fits in with the overall design of the flyer. I don't want you to simply cut and paste my basic table into the design.

In terms of what needs to be included, I have tried to be as specific as possible here but please feel free to message me if you need any further information or clarification.

FRONT SIDE:
The title of our service is:
Expert Lawn Treatment Service

Our strapline will need to be included somewhere:
"Lawn care by your local gardening expert"

The front side of the flyer will need to contain our logo - different versions of which can be found within my dropbox folder here...

https://www.sharebinnu.co.uk/sh/k7qd21mzplax/QRT8xWbnNeLu4Pa-ZxYyhKcLo?dl=0

The front side will need to contain a main image (although feel free to add more if you have anything suitable). I have included a picture in the dropbox folder titled "Front side image" which we would like used. I've also included in the folder an adobe image of grass which you may or may not like to use on either front or back.

Somewhere on both the front and back sides, you will need to include our contact details:
01632 960417
www.tavistrowgardening.co.uk/lawncare

The front side should show what treatments we currently have available. These are:

- Lawn Fertilising
- Scarification
- Aeration
- Weed Control
- Moss Control
- Hydration Booster
- PlumeRest
- Turfing & Renovation

"Select a one-off treatment or choose from one of our specially created lawn care packages."

BACK SIDE:
On the back, we will still need our logo and contact details but the image we'd like used should be the one in the dropbox folder titled "Back side image". Again, if you have any other images you feel would also work, then please feel free to add them.

The back side is to contain a bit more information and be a bit 'wordier' and so can you please include the following 2 paragraphs:

"As expert gardeners, we are passionate about horticulture and working to bring out the very best in your garden. When we work in your garden, we look at it and treat it with the same care and attention as if it were our own, before handing it back for you to enjoy. Our passion doesn't end at just trees and shrubs though. Your grass is as much of a living, breathing plant as your shrubs and we therefore utilise our expert horticultural knowledge to ensure your lawn thrives and reaches its fullest potential.

Lawn care isn't just about applying a fertiliser. It's about really understanding your lawn and being able to use extensive knowledge and experience to diagnose and treat issues. It therefore stands to reason that you should employ an expert to bring out the best in your lawn which is why we at Tavistrow Gardening Services have created a superior lawn care service that will keep your lawn looking lush, green and healthy all year round."

I referred at the very top of this brief to the fact we will need an infographic table created to show the different lawn care packages available. You see from the PDF table I created that we have 3 packages; Standard, Enhanced and Premium. Please create a visually appealing table which sets out the differences between our packages and include it on the back page.

Finally, somewhere we would like reference to the other gardening services we do. It's only to be something small as it isn't the main focus of the flyer but we think it would be good to mention what else we do. To re-iterate, it isnt to be big. I still want the main focus to be lawn care but if you could somehow reference that we also do the following services, that would be good. I will leave it to you to decide where on the flyer it fits in best, be it the front or back:

- Lawn mowing
- Shrub pruning
- Hedge trimming
- Weed killing
- Garden clearance & tidy-up
- Planting & design
- Regular Garden Maintenance
- Turfing
- Fencing
- Gutter clearance

I think thats it. I look forward to your designs!
Ps. Don't forget the dropbox folder:

Target Market(s)

Professional men/women aged 25+
Retired aged 65+

Industry/Entity Type

Home And Garden

Font styles to use
Sans Serif

Colors
6b449b
9bcb3c

Requirements
Must have
• Our company colours; purple and green; as per our website www.tavistrowgardening.co.uk. I've selected purple and green on this brief just to highlight the colours needed but please be sure to use the exact shades from our website and NOT the shade of purple and green that were selected on this brief.
• All the wording as explained in the main project brief.
Nice to have
• I want the flyer to be bold, eye-catching and modern.
• We particularly like the font Trebuchet MS for general copy but please feel free to use any other font for bolder, main titles.
Should not have
• We don't want anything gimmicky. No cheesy marketing.
• We only want professional looking designs. With the greatest of respect, if you're just starting out or don't really do design but think you'll use this as practise, please don't waste your or our time. We've previously run contests for other projects where we've had designs submitted that have clearly been done on MS Word and used Clipart and Wordart. That's really not what we are looking for.

```html
<!DOCTYPE html>
<html lang="en">
<head>
<meta charset="utf-8">
<title>Tavistrow Gardening Services – Lawn Treatment Flyer</title>
<link href="https://fonts.googleapis.com/css2?family=Roboto+Condensed:ital,wght@0,400;0,700;1,400;1,700&family=Questrial&display=swap" rel="stylesheet">
<style>
  :root {
    --purple: #7b2d8e;
    --purple-dark: #6a2479;
    --green: #4c9a2f;
    --green-deep: #2f7b36;
    --green-band: #2d7e3a;
    --lime: #8dc63f;
    --paving: #b9b8b0;
    --white: #ffffff;
    --ink: #3b3b3b;
    --backdrop: #e8e6e1;
  }
  * { box-sizing: border-box; margin: 0; padding: 0; }
  html, body { width: 1200px; height: 1200px; overflow: hidden; }
  body { background: var(--backdrop); font-family: "Roboto Condensed", Arial, sans-serif; position: relative; }

  .flyer { position: absolute; width: 526px; height: 745px; background: var(--white); overflow: hidden; box-shadow: 0 6px 18px rgba(0,0,0,.18); }
  .flyer--front { left: 54px; top: 67px; }
  .flyer--back { left: 623px; top: 379px; }
  .abs { position: absolute; }

  .brand { display: flex; align-items: center; gap: 8px; color: var(--green-deep); }
  .brand__dot { width: 16px; height: 16px; border-radius: 50%; background: var(--lime); flex: none; }
  .brand__name { font-family: "Questrial", Arial, sans-serif; font-size: 22px; line-height: 1.1; }
  .divider { width: 2px; background: var(--purple); }
  .strapline { color: var(--purple); font-weight: 700; font-style: italic; text-transform: uppercase; line-height: 1.14; }

  .photo { background: linear-gradient(160deg, #8ab86a 0%, #5fa63a 35%, #479b2c 70%, #3d8d27 100%); }
  .curve-mask { position: absolute; left: 0; width: 100%; }

  /* front */
  .front-title { left: 55px; top: 219px; color: var(--white); text-shadow: 0 2px 3px rgba(0,0,0,.35); }
  .front-title__main { font-size: 43px; font-weight: 700; line-height: 1; }
  .front-title__sub { font-size: 29px; line-height: 1.05; }
  .treatments { left: 41px; top: 298px; width: 234px; height: 255px; background: var(--purple); border-radius: 14px 14px 0 0; padding: 22px 0 0 16px; list-style: none; }
  .treatments::after { content: ""; position: absolute; right: -16px; top: 87px; border-left: 18px solid var(--purple); border-top: 14px solid transparent; border-bottom: 0 solid transparent; border-top-width: 0; border-bottom-width: 14px; border-bottom-color: transparent; }
  .treatments li { color: var(--white); font-size: 20px; line-height: 27.6px; display: flex; align-items: center; gap: 10px; }
  .tick { width: 18px; height: 16px; flex: none; }
  .front-offer { left: 297px; top: 398px; width: 210px; color: var(--white); font-style: italic; font-size: 12.2px; line-height: 16.5px; }
  .front-call { left: 297px; top: 452px; color: var(--white); font-style: italic; font-size: 14.6px; line-height: 19px; text-transform: uppercase; }
  .front-phone { left: 297px; top: 492px; color: var(--white); font-size: 33px; font-weight: 700; letter-spacing: .5px; }
  .team-scene { left: 0; top: 553px; width: 100%; height: 132px; background: linear-gradient(180deg, #d9eec4 0%, #b5db8b 55%, #8cc45a 100%); }
  .footer { left: 0; top: 685px; width: 100%; height: 60px; background: var(--purple); color: var(--white); text-align: center; font-size: 14.5px; letter-spacing: 2.6px; font-weight: 700; padding-top: 13px; }
  .flyer--back .footer { top: 685px; }

  /* back */
  .intro { left: 0; top: 140px; width: 100%; height: 214px; background: linear-gradient(180deg, #3f8f3b 0%, #2f7e36 100%); }
  .intro__text { left: 33px; top: 168px; width: 466px; color: var(--white); font-size: 11.3px; line-height: 15.2px; }
  .intro__text p + p { margin-top: 15px; }
  .package-head { left: 0; top: 353px; width: 100%; height: 30px; background: var(--purple); }
  .package-head span { position: absolute; top: 7px; color: var(--white); font-weight: 700; font-size: 12px; letter-spacing: .4px; }
  .grid-bg { left: 0; top: 383px; width: 100%; height: 252px; background: linear-gradient(90deg, var(--paving) 0%, #8fb874 30%, #5ea33e 55%, #a9aba2 80%, #7aa760 100%); }
  .row-band { position: absolute; left: 0; width: 100%; height: 50px; background: var(--green-band); }
  .cell { position: absolute; width: 140px; height: 66px; }
  .cell__thumb { position: absolute; left: 0; top: 0; width: 64px; height: 64px; border: 3px solid var(--white); background: linear-gradient(160deg, #9bc77a, #4f9a33); }
  .cell__label { position: absolute; left: 72px; top: 4px; color: var(--white); font-weight: 700; font-size: 12px; line-height: 15px; text-transform: uppercase; }
  .badges { position: absolute; right: 76px; bottom: -7px; display: flex; gap: 4px; }
  .badge { width: 18px; height: 18px; border-radius: 50%; background: var(--purple); border: 1.5px solid var(--white); color: var(--white); font-size: 8.5px; display: flex; align-items: center; justify-content: center; }
  .back-call { left: 0; top: 635px; width: 100%; height: 50px; background: var(--white); }
  .back-call__label { position: absolute; right: 283px; top: 9px; text-align: right; color: var(--green); font-style: italic; font-weight: 700; font-size: 14px; line-height: 18px; text-transform: uppercase; }
  .back-call__phone { position: absolute; left: 253px; top: 2px; color: var(--purple); font-weight: 700; font-size: 39px; }
</style>
</head>
<body>

<!-- FRONT SIDE -->
<section class="flyer flyer--front">
  <div class="abs brand" style="left:50px; top:80px;">
    <span class="brand__dot"></span>
    <span class="brand__name">Tavistrow<br>Gardening Services</span>
  </div>
  <div class="abs divider" style="left:288px; top:66px; height:90px;"></div>
  <p class="abs strapline" style="left:302px; top:74px; font-size:22px;">Lawn care by<br>your local<br>gardening expert</p>

  <div class="abs photo" style="left:0; top:160px; width:100%; height:400px;" role="img" aria-label="Green lawn with a winding paved garden path and flower beds"></div>
  <svg class="curve-mask" style="top:158px;" width="526" height="40" viewBox="0 0 526 40" preserveAspectRatio="none">
    <path d="M0 0 H526 V36 C400 6 160 4 0 22 Z" fill="#ffffff"/>
  </svg>

  <div class="abs front-title">
    <div class="front-title__main">Expert Lawn</div>
    <div class="front-title__sub">Treatment Service</div>
  </div>

  <ul class="abs treatments">
    <li><svg class="tick" viewBox="0 0 18 16"><path d="M1 9 L6 14 L17 2" fill="none" stroke="#fff" stroke-width="3.5"/></svg>Lawn Fertilising</li>
    <li><svg class="tick" viewBox="0 0 18 16"><path d="M1 9 L6 14 L17 2" fill="none" stroke="#fff" stroke-width="3.5"/></svg>Scarification</li>
    <li><svg class="tick" viewBox="0 0 18 16"><path d="M1 9 L6 14 L17 2" fill="none" stroke="#fff" stroke-width="3.5"/></svg>Aeration</li>
    <li><svg class="tick" viewBox="0 0 18 16"><path d="M1 9 L6 14 L17 2" fill="none" stroke="#fff" stroke-width="3.5"/></svg>Weed Control</li>
    <li><svg class="tick" viewBox="0 0 18 16"><path d="M1 9 L6 14 L17 2" fill="none" stroke="#fff" stroke-width="3.5"/></svg>Moss Control</li>
    <li><svg class="tick" viewBox="0 0 18 16"><path d="M1 9 L6 14 L17 2" fill="none" stroke="#fff" stroke-width="3.5"/></svg>Hydration Booster</li>
    <li><svg class="tick" viewBox="0 0 18 16"><path d="M1 9 L6 14 L17 2" fill="none" stroke="#fff" stroke-width="3.5"/></svg>PlumeRest</li>
    <li><svg class="tick" viewBox="0 0 18 16"><path d="M1 9 L6 14 L17 2" fill="none" stroke="#fff" stroke-width="3.5"/></svg>Turfing &amp; Renovation</li>
  </ul>

  <p class="abs front-offer">Select a one-off treatment or choose from one of our specially created lawn care packages.</p>
  <p class="abs front-call">Call Tavistrow Gardening<br>Services Ltd on</p>
  <p class="abs front-phone">01632 960417</p>

  <div class="abs team-scene" role="img" aria-label="Silhouettes of gardeners mowing, raking, planting and pruning among trees"></div>
  <svg class="curve-mask" style="top:540px;" width="526" height="30" viewBox="0 0 526 30" preserveAspectRatio="none">
    <path d="M0 30 V18 C180 -2 380 0 526 14 V30 Z" fill="#d9eec4"/>
  </svg>

  <div class="abs footer">www.tavistrowgardening.co.uk/lawncare</div>
</section>

<!-- BACK SIDE -->
<section class="flyer flyer--back">
  <div class="abs brand" style="left:70px; top:56px;">
    <span class="brand__dot"></span>
    <span class="brand__name" style="font-size:19px;">Tavistrow<br>Gardening Services</span>
  </div>
  <div class="abs divider" style="left:275px; top:47px; height:75px;"></div>
  <p class="abs strapline" style="left:286px; top:54px; font-size:18px; line-height:1.25;">Lawn care by<br>your local<br>gardening expert</p>

  <div class="abs intro" role="img" aria-label="Lawn and garden path photograph under a green tint"></div>
  <svg class="curve-mask" style="top:138px;" width="526" height="34" viewBox="0 0 526 34" preserveAspectRatio="none">
    <path d="M0 0 H526 V8 C380 -2 160 4 0 26 Z" fill="#ffffff"/>
  </svg>
  <div class="abs intro__text">
    <p>"As expert gardeners, we are passionate about horticulture and working to bring out the very best in your garden. When we work in your garden, we look at it and treat it with the same care and attention as if it were our own, before handing it back for you to enjoy. Our passion doesn't end at just trees and shrubs though. Your grass is as much of a living, breathing plant as your shrubs and we therefore utilise our expert horticultural knowledge to ensure your lawn thrives and reaches its fullest potential.</p>
    <p>Lawn care isn't just about applying a fertiliser. It's about really understanding your lawn and being able to use extensive knowledge and experience to diagnose and treat issues. It therefore stands to reason that you should employ an expert to bring out the best in your lawn which is why we at Tavistrow Gardening Services have created a superior lawn care service that will keep your lawn looking lush, green and healthy all year round."</p>
  </div>

  <div class="abs package-head">
    <span style="left:41px;">STANDARD PACKAGE</span>
    <span style="left:186px;">ENHANCED PACKAGE</span>
    <span style="left:336px;">PREMIUM PACKAGE</span>
  </div>

  <div class="abs grid-bg" role="img" aria-label="Paved garden path between green lawns and flower borders">
    <div class="row-band" style="top:8px;"></div>
    <div class="row-band" style="top:94px;"></div>
    <div class="row-band" style="top:177px;"></div>

    <div class="cell" style="left:37px; top:6px;">
      <div class="cell__thumb" role="img" aria-label="Lawn spreader on grass"></div>
      <div class="cell__label">Spring<br>Treatment</div>
      <div class="badges"><span class="badge">SP</span><span class="badge">EP</span><span class="badge">PP</span></div>
    </div>
    <div class="cell" style="left:182px; top:6px;">
      <div class="cell__thumb" role="img" aria-label="Garden path through summer lawn"></div>
      <div class="cell__label">Early<br>Summer<br>Treatment</div>
      <div class="badges"><span class="badge">SP</span><span class="badge">EP</span><span class="badge">PP</span></div>
    </div>
    <div class="cell" style="left:330px; top:6px;">
      <div class="cell__thumb" role="img" aria-label="Striped mown lawn"></div>
      <div class="cell__label">Late<br>Summer<br>Treatment</div>
      <div class="badges"><span class="badge">SP</span><span class="badge">EP</span><span class="badge">PP</span></div>
    </div>

    <div class="cell" style="left:37px; top:92px;">
      <div class="cell__thumb" role="img" aria-label="Spreader applying autumn feed"></div>
      <div class="cell__label">Autumn/<br>Winter<br>Treatment</div>
      <div class="badges"><span class="badge">SP</span><span class="badge">EP</span><span class="badge">PP</span></div>
    </div>
    <div class="cell" style="left:182px; top:92px;">
      <div class="cell__thumb" role="img" aria-label="Lawn aerator machine at work"></div>
      <div class="cell__label">Aeration</div>
      <div class="badges"><span class="badge">EP</span><span class="badge">PP</span></div>
    </div>
    <div class="cell" style="left:330px; top:92px;">
      <div class="cell__thumb" role="img" aria-label="Scarifier removing thatch from lawn"></div>
      <div class="cell__label">Scarification</div>
      <div class="badges"><span class="badge">EP</span><span class="badge">PP</span></div>
    </div>

    <div class="cell" style="left:37px; top:175px;">
      <div class="cell__thumb" role="img" aria-label="Close-up of fresh lawn"></div>
      <div class="cell__label">PlumeRest</div>
      <div class="badges"><span class="badge">PP</span></div>
    </div>
    <div class="cell" style="left:182px; top:175px;">
      <div class="cell__thumb" role="img" aria-label="Dew drops on grass blades"></div>
      <div class="cell__label">Hydration<br>Boost</div>
      <div class="badges"><span class="badge">PP</span></div>
    </div>
    <div class="cell" style="left:330px; top:175px;">
      <div class="cell__thumb" role="img" aria-label="Roll of new turf being laid"></div>
      <div class="cell__label">Turfing &amp;<br>Renovation</div>
      <div class="badges"><span class="badge">PP</span></div>
    </div>
  </div>

  <div class="abs back-call">
    <p class="back-call__label">Call Tavistrow Gardening<br>Services Ltd on</p>
    <p class="back-call__phone">01632 960417</p>
  </div>

  <div class="abs footer">www.tavistrowgardening.co.uk/lawncare</div>
</section>

</body>
</html>
```